Business card design for Velvet Harbor

We need business cards designed for our new marketing consulting company, Velvet Harbor. Our services include marketing strategy, go-to-market and launch planning, growth strategy, and execution. We serve medical technology and health technology companies, from startups to well-established growth companies.

The business cards should feel professional, credible, reliable and trustworthy, and should instill confidence. Also bold, creative, and modern.

The design must use the Velvet Harbor logo.

The primary brand color is this orange: #FF5501
A secondary color that you can use is this gray: #282B2D
I would prefer only to use the orange and gray. But if you feel you really need an additional accent color (please use it very sparingly, as little as possible), you can use this blue for small accent purposes: #009FED

Attached are the logo files. The main logo is the one with a little bit of orange on the left and the rest is gray.

The business card should include the following:

Velvet Harbor logo
First name and last name
Title
Email address
Phone number and type (in whatever order looks best for the design
Website (the website does not need to be in the same block as the personal info)

For example:

Nessa Pryle
Founder & Principal
nessa@velvetharbor.com
+1.628.309.4156 mobile (can use "." or spaces in between blocks of numbers)
velvetharbor.com (somewhere on the card, it does not need to be with the personal info; and note that there is no "www." at the beginning)

Note that there will be no address listed on the business card.

Target Market(s)

Executives (CEO, head of marketing, head of sales) at medical technology and health technology companies, mostly in their 40s and older, well-educated, often with advanced degrees. They are strategic thinkers, responsible for budgets, and familiar with P&L. Their comfort with and trust in using outside consultants varies.

Industry/Entity Type

Medical technology and health technology companies.

Contact Information for Business Card

See project description

Font styles to use
Sans Serif

Requirements
Must have
• Logo and see Business card details section above.

```html
<!DOCTYPE html>
<html lang="en">
<head>
<meta charset="utf-8">
<title>Velvet Harbor — Business Card</title>
<link href="https://fonts.googleapis.com/css2?family=Montserrat:wght@400;600;700&display=swap" rel="stylesheet">
<style>
  :root {
    --stage: #3a3a3a;
    --card: #141414;
    --orange: #ff5501;
    --white: #f2f2f2;
    --muted: #d9d9d9;
    --deboss: #060606;
  }
  * { box-sizing: border-box; margin: 0; padding: 0; }
  html, body { width: 1200px; height: 801px; overflow: hidden; }
  body {
    background: var(--stage);
    font-family: "Montserrat", sans-serif;
    display: flex;
    align-items: center;
    justify-content: center;
    gap: 40px;
  }
  .card {
    position: relative;
    width: 525px;
    height: 300px;
    background: var(--card);
    border-bottom: 3px solid var(--orange);
    border-right: 3px solid var(--orange);
    box-shadow: 0 12px 30px rgba(0,0,0,.35);
  }
  .brand {
    display: flex;
    align-items: center;
    gap: 18px;
  }
  .brand-dot {
    width: 64px;
    height: 64px;
    border-radius: 50%;
    border: 7px solid var(--white);
    flex: none;
  }
  .brand-name {
    font-weight: 700;
    font-size: 34px;
    line-height: 1.05;
    letter-spacing: 6px;
    text-transform: uppercase;
    color: var(--white);
  }
  .card-front .brand { position: absolute; left: 40px; top: 42px; }
  .person { position: absolute; left: 40px; bottom: 44px; }
  .person-name {
    color: var(--orange);
    font-weight: 700;
    font-size: 21px;
    letter-spacing: 1px;
    text-transform: uppercase;
  }
  .person-title { color: var(--white); font-size: 15px; margin-top: 4px; }
  .divider {
    position: absolute;
    left: 268px;
    top: 172px;
    width: 1px;
    height: 80px;
    background: var(--orange);
  }
  .contact {
    position: absolute;
    left: 292px;
    top: 176px;
    list-style: none;
    color: var(--muted);
    font-size: 13.5px;
  }
  .contact li { display: flex; align-items: center; gap: 9px; height: 24px; }
  .contact svg { width: 12px; height: 12px; flex: none; }
  .card-back .brand {
    position: absolute;
    left: 50%;
    top: 50%;
    transform: translate(-50%, -50%);
  }
  .card-back .brand-dot { border-color: var(--deboss); }
  .card-back .brand-name { color: var(--deboss); }
</style>
</head>
<body>
  <section class="card card-front">
    <div class="brand">
      <span class="brand-dot"></span>
      <span class="brand-name">Velvet<br>Harbor</span>
    </div>
    <div class="person">
      <p class="person-name">Nessa Pryle</p>
      <p class="person-title">Founder &amp; Principal</p>
    </div>
    <span class="divider"></span>
    <ul class="contact">
      <li>
        <svg viewBox="0 0 12 12" aria-hidden="true"><path fill="var(--orange)" d="M2.5 1l2 2-1 1.3a6 6 0 0 0 3.2 3.2L8 6.5l2 2-1.3 1.8C5 10 2 7 1.7 3.3z"/></svg>
        +1.628.309.4156
      </li>
      <li>
        <svg viewBox="0 0 12 12" aria-hidden="true"><rect x="1" y="2.5" width="10" height="7" fill="var(--orange)"/><path d="M1 2.5l5 4 5-4" fill="none" stroke="var(--card)" stroke-width="1"/></svg>
        nessa@velvetharbor.com
      </li>
      <li>
        <svg viewBox="0 0 12 12" aria-hidden="true"><circle cx="6" cy="6" r="5" fill="var(--orange)"/><path d="M1 6h10M6 1c-2.5 3-2.5 7 0 10M6 1c2.5 3 2.5 7 0 10" fill="none" stroke="var(--card)" stroke-width=".8"/></svg>
        velvetharbor.com
      </li>
    </ul>
  </section>

  <section class="card card-back">
    <div class="brand">
      <span class="brand-dot"></span>
      <span class="brand-name">Velvet<br>Harbor</span>
    </div>
  </section>
</body>
</html>
```